KORA product web page

We need a new web design for our KORA product page. You can find more information about the project on the current web site - www.kora-example.io

What we need from a new design (uncoded):
- landing pages + template
- all information on one page
- the design should be focused on the product - light bulb + app
- web site should be with some dynamics like a background with parallax effect in the current version
- fonts should be chosen
- a number of illustrations should be designed

Here is schema for a new design: https://files.example-share.net/drawings/d/7Qx2mPa91LzR4tHwKc8NvB3yUe6JdF0sGiXoAqWbYnV/edit

Here is a document with all texts for a new design: https://files.example-share.net/document/d/5Rt8kLm20WqZ7yHcVb4NxP1sGe9JdA3uTiFoKpQbMnC/edit

Illustrations to use:
v1 - https://store.example-share.net/folder?id=9Z4PkRwaLtYq7M118N2CVXTonOpa
v2 - https://store.example-share.net/folder?id=9Z4PkRwaLtYq7bWkuPp3C5aJgRs

Orbit OS screens: https://store.example-share.net/folder?id=9H3t7QC5Jh4wLTyq8Vm2NxQaKR7S

KORA logo: https://store.example-share.net/folder?id=9Z4PkRwaLtYq7gT2XV6N4dmoqOih
Updates

I forgot to add the definition text "KORA - is.." to the document with texts. Sorry, my mistake.

Target Market(s)

25-45 year old adults who are interested in "smart" devices for their health.

Industry/Entity Type

Google

Colors

Designer to choose colors to be used in the design.

Requirements
Must have
• - landing pages + template
- fonts should be chosen

```html
<!DOCTYPE html>
<html lang="en">
<head>
<meta charset="utf-8">
<title>KORA — smart true color lighting</title>
<link rel="stylesheet" href="https://fonts.googleapis.com/css2?family=Open+Sans:wght@300;400;600;700&display=swap">
<style>
:root{
  --ink:#040a14;
  --navy:#071a33;
  --navy-deep:#050f20;
  --band:#0b2545;
  --blue:#2aa2f0;
  --button:#1b82d6;
  --white:#ffffff;
  --muted:#9fb3c8;
  --line:rgba(120,170,220,.25);
  --card:rgba(8,22,42,.85);
}
*{box-sizing:border-box;margin:0;padding:0}
html,body{width:1200px;height:4304px;overflow:hidden}
body{position:relative;background:var(--navy-deep);font-family:"Open Sans",Arial,sans-serif;color:var(--white)}
.abs{position:absolute}
section,header,footer{position:absolute;left:0;width:1200px;overflow:hidden}

/* nav */
.site-nav{top:0;height:80px;background:var(--ink);border-bottom:1px solid #1a2a40}
.site-nav a{position:absolute;top:30px;font-size:13px;color:var(--white);text-decoration:none;letter-spacing:.5px;text-transform:uppercase}
.brand{position:absolute;left:540px;top:16px;width:120px;text-align:center;font-size:34px;font-weight:700;letter-spacing:3px;color:var(--white);line-height:48px}

.band{background:radial-gradient(ellipse at 70% 40%,#123a66 0%,var(--navy) 45%,var(--navy-deep) 100%)}
.band-alt{background:radial-gradient(ellipse at 30% 50%,#0f3260 0%,var(--navy) 50%,var(--navy-deep) 100%)}
.band-light{background:linear-gradient(180deg,#0d2b52,#113868 50%,#0d2b52)}
.sep{border-top:1px solid var(--line)}

.title{font-weight:700;color:var(--blue);text-transform:uppercase;letter-spacing:.5px}
.btn{display:block;width:148px;height:36px;line-height:36px;text-align:center;background:var(--button);color:var(--white);font-size:14px;border-radius:3px;text-decoration:none}
.visual{border-radius:18px}

.dots{position:absolute;left:1134px;width:12px}
.dots span{display:block;width:10px;height:10px;border-radius:50%;border:1px solid var(--white);margin-bottom:14px}
.dots span.on{background:var(--white)}

/* hero */
.hero{top:80px;height:680px}
.hero .title{left:144px;top:192px;font-size:36px}
.hero p{left:144px;top:238px;width:560px;font-size:20px;line-height:28px}
.hero .btn{left:144px;top:350px}
.hero .visual{left:760px;top:40px;width:400px;height:560px;background:radial-gradient(ellipse at 45% 25%,#ffd34d 0%,#f0a520 18%,#3d4a5e 40%,rgba(30,45,70,.4) 70%,transparent 80%)}
.scroll-down{left:570px;top:510px}

/* what we do */
.what{top:760px;height:620px}
.what .title{left:0;width:1200px;text-align:center;top:40px;font-size:48px}
.what .lead{left:0;width:1200px;text-align:center;top:110px;font-size:24px}
.card{position:absolute;top:200px;width:260px;height:360px;background:var(--card);border:1px solid var(--line);padding:40px 26px 0;text-align:center}
.card svg{display:block;margin:0 auto 28px}
.card h3{font-size:18px;font-weight:600;text-transform:uppercase;margin-bottom:18px}
.card p{font-size:12px;line-height:19px;color:var(--muted)}

/* app */
.app{top:1380px;height:620px}
.app .visual{left:80px;top:40px;width:460px;height:480px;background:radial-gradient(ellipse at 30% 30%,#f5e06a 0%,#e0c030 14%,transparent 32%),radial-gradient(ellipse at 65% 35%,#7fd4ff 0%,#2aa2f0 15%,transparent 33%),radial-gradient(ellipse at 50% 65%,#4a5566 0%,transparent 55%)}
.app .title{left:592px;top:200px;font-size:36px}
.pill-list{position:absolute;left:592px;top:262px;list-style:none}
.pill-list li{border:1px solid var(--line);background:rgba(5,15,30,.6);padding:6px 14px;font-size:18px;margin-bottom:8px;width:max-content}
.pill-list li::before{content:"";display:inline-block;width:7px;height:7px;border-radius:50%;background:var(--white);margin-right:12px;vertical-align:middle}
.app .btn{left:592px;top:456px}

/* health */
.health{top:2000px;height:560px}
.health .title{left:144px;top:160px;font-size:32px}
.dot-list{position:absolute;list-style:none}
.dot-list li{font-size:15px;margin-bottom:16px}
.dot-list li::before{content:"";display:inline-block;width:6px;height:6px;border-radius:50%;background:var(--white);margin-right:12px;vertical-align:middle}
.health .dot-list{left:144px;top:225px}
.health .btn{left:144px;top:400px}
.health .visual{left:800px;top:70px;width:360px;height:420px;background:linear-gradient(160deg,#dfe8f2 0%,#b7c6d6 40%,#2b3a50 75%,transparent 100%);opacity:.9}

/* lighting design */
.design{top:2560px;height:480px}
.design .visual.bulbs{left:80px;top:40px;width:280px;height:400px;background:radial-gradient(ellipse at 30% 25%,#8fe0ff 0%,#3aa8e8 16%,transparent 34%),radial-gradient(ellipse at 55% 55%,#ff4040 0%,#c01818 12%,transparent 28%),radial-gradient(ellipse at 50% 75%,#3e4858 0%,transparent 55%)}
.design .title{left:592px;top:80px;font-size:36px}
.design p{position:absolute;left:592px;width:400px;font-size:14px;line-height:21px;color:#d4e0ec}
.design .visual.lamp{left:1010px;top:200px;width:150px;height:220px;background:radial-gradient(ellipse at 50% 80%,#ffffff 0%,#d8e4f0 18%,#3a4658 45%,transparent 75%)}

/* and health */
.care{top:3040px;height:600px}
.care .title{left:144px;top:40px;font-size:32px}
.tick-list{position:absolute;left:144px;top:100px;width:540px;list-style:none}
.tick-list li{position:relative;padding-left:26px;font-size:13px;line-height:18px;margin-bottom:18px}
.tick-list li svg{position:absolute;left:0;top:3px}
.care .btn{left:144px;top:440px}
.care .visual{left:720px;top:140px;width:440px;height:440px;background:linear-gradient(150deg,#e6edf5 0%,#c3d1df 35%,#4a6fa0 60%,transparent 95%);opacity:.9}

/* specs */
.specs{top:3640px;height:360px}
.specs .visual{left:240px;top:20px;width:200px;height:320px;background:radial-gradient(ellipse at 50% 25%,#ffe27a 0%,#f2b426 22%,#4a5466 50%,transparent 78%)}
.specs .title{left:472px;top:30px;font-size:24px}
.specs .dot-list{left:472px;top:78px;width:480px}
.specs .dot-list li{font-size:13px;line-height:18px;margin-bottom:12px}

/* footer */
.site-footer{top:4000px;height:304px;background:var(--ink)}
.site-footer h2{position:absolute;left:0;width:1200px;text-align:center;top:30px;font-size:30px;font-weight:300;letter-spacing:1px}
.social{position:absolute;left:450px;top:92px;display:flex;gap:16px}
.social span{width:44px;height:44px;border-radius:50%;border:2px solid var(--white)}
.site-footer .rule{position:absolute;left:300px;top:190px;width:600px;border-top:1px solid #1f2d40}
.site-footer small{position:absolute;left:0;width:1200px;text-align:center;top:232px;font-size:12px;color:var(--muted)}
</style>
</head>
<body>

<header class="site-nav">
  <a href="#" style="left:170px">Pre-order</a>
  <a href="#" style="left:358px">Blog</a>
  <div class="brand">KORA</div>
  <a href="#" style="left:790px">Contacts</a>
  <a href="#" style="left:966px">RU</a>
</header>

<section class="hero band">
  <h1 class="abs title">KORA is you comfort</h1>
  <p class="abs">KORA is the right lighting designed especialy for your health and comfort: a smart true color linkwave enabled LED light bulb.</p>
  <a class="abs btn" href="#">Read More</a>
  <div class="abs visual" role="img" aria-label="Glowing yellow KORA smart bulb beside a smartphone showing the app"></div>
  <svg class="abs scroll-down" width="60" height="60" viewBox="0 0 60 60"><circle cx="30" cy="30" r="28" fill="none" stroke="#fff" stroke-width="2"/><path d="M19 25 L30 36 L41 25" fill="none" stroke="#fff" stroke-width="3"/></svg>
</section>

<section class="what band-alt sep">
  <h2 class="abs title">What we do</h2>
  <p class="abs lead">Control KORA lightbulbs with your mobile device</p>
  <div class="dots" style="top:240px"><span class="on"></span><span></span><span></span><span></span><span></span></div>
  <article class="card" style="left:160px">
    <svg width="60" height="60" viewBox="0 0 60 60" fill="#2aa2f0"><rect x="4" y="4" width="14" height="14"/><rect x="23" y="4" width="14" height="14"/><rect x="42" y="4" width="14" height="14"/><rect x="4" y="23" width="14" height="14"/><rect x="23" y="23" width="14" height="14"/><rect x="42" y="23" width="14" height="14"/><rect x="4" y="42" width="14" height="14"/><rect x="23" y="42" width="14" height="14"/><rect x="42" y="42" width="14" height="14"/></svg>
    <h3>KORA App</h3>
    <p>KORA application allows you to control each lightbulb at home, manage your lighting by creating scenes and setting schedules for comfort.</p>
  </article>
  <article class="card" style="left:470px">
    <svg width="60" height="60" viewBox="0 0 60 60"><path d="M30 5 C14 5 4 17 4 30 C4 44 15 55 28 55 C34 55 34 49 30 46 C27 43 29 38 34 38 L44 38 C52 38 56 32 56 26 C56 14 44 5 30 5Z" fill="#2aa2f0"/><circle cx="18" cy="24" r="4" fill="#071a33"/><circle cx="28" cy="15" r="4" fill="#071a33"/><circle cx="41" cy="18" r="4" fill="#071a33"/><circle cx="16" cy="38" r="4" fill="#071a33"/></svg>
    <h3>KORA Color</h3>
    <p>Experiment with millions of colors from the color wheel of your mobile device and set the perfect mood for every room.</p>
  </article>
  <article class="card" style="left:780px">
    <svg width="60" height="60" viewBox="0 0 60 60" fill="#2aa2f0"><path d="M30 4 C19 4 12 12 12 22 C12 30 18 34 21 40 L39 40 C42 34 48 30 48 22 C48 12 41 4 30 4Z"/><rect x="21" y="43" width="18" height="4"/><rect x="21" y="49" width="18" height="4"/><rect x="25" y="55" width="10" height="3"/></svg>
    <h3>KORA</h3>
    <p>KORA lightbulb is a 9W LED equivalent to a 60W incandescent bulb that saves energy and fits any standard socket.</p>
  </article>
</section>

<section class="app band sep">
  <div class="abs visual" role="img" aria-label="Two KORA bulbs glowing yellow and light blue"></div>
  <h2 class="abs title">KORA App</h2>
  <ul class="pill-list">
    <li>Control KORA lightbulbs with your mobile device</li>
    <li>Orbit OS devices with Linkwave 4 (LE)</li>
    <li>Nimbus OS devices with Linkwave 2.1 or 4</li>
    <li>5W incandescent equivalent</li>
  </ul>
  <a class="abs btn" href="#">Read More</a>
  <div class="dots" style="top:240px"><span></span><span class="on"></span><span></span><span></span><span></span></div>
</section>

<section class="health band-alt sep">
  <h2 class="abs title">KORA Health</h2>
  <ul class="dot-list">
    <li>Control KORA lightbulbs with your mobile device</li>
    <li>Orbit OS devices with Linkwave 4 (LE)</li>
    <li>Nimbus OS devices with Linkwave 2.1 or 4</li>
    <li>5W incandescent equivalent</li>
  </ul>
  <a class="abs btn" href="#">Read More</a>
  <div class="abs visual" role="img" aria-label="Two smartphones showing KORA app lighting screens"></div>
  <div class="dots" style="top:200px"><span></span><span></span><span class="on"></span><span></span><span></span></div>
</section>

<section class="design band">
  <div class="abs visual bulbs" role="img" aria-label="KORA bulbs glowing light blue and red"></div>
  <h2 class="abs title">Lightning design</h2>
  <p style="top:140px">Wireless lightbulbs with Linkwave bring a new way to experience light at home, simple to set up and easy to control.</p>
  <p style="top:220px">Create the perfect lighting for each room: warm tones for the bedroom, bright light for the kitchen and soft colors for the evening.</p>
  <div class="abs visual lamp" role="img" aria-label="KORA bulb glowing white, seen from below"></div>
  <div class="dots" style="top:100px"><span></span><span></span><span></span><span class="on"></span><span></span></div>
</section>

<section class="care band-alt sep">
  <h2 class="abs title">KORA and Health</h2>
  <ul class="tick-list">
    <li><svg width="14" height="12" viewBox="0 0 14 12"><path d="M1 6 L5 10 L13 1" fill="none" stroke="#fff" stroke-width="2"/></svg>KORA lightbulb is a 9W LED equivalent that transforms your visual environment.</li>
    <li><svg width="14" height="12" viewBox="0 0 14 12"><path d="M1 6 L5 10 L13 1" fill="none" stroke="#fff" stroke-width="2"/></svg>E27 socket: no need to change anything, easy to fit in any home lamp.</li>
    <li><svg width="14" height="12" viewBox="0 0 14 12"><path d="M1 6 L5 10 L13 1" fill="none" stroke="#fff" stroke-width="2"/></svg>16 million colors and 600 lumens of brightness from an energy efficient LED.</li>
    <li><svg width="14" height="12" viewBox="0 0 14 12"><path d="M1 6 L5 10 L13 1" fill="none" stroke="#fff" stroke-width="2"/></svg>2700-5500K: choose the white temperature that suits your mood.</li>
    <li><svg width="14" height="12" viewBox="0 0 14 12"><path d="M1 6 L5 10 L13 1" fill="none" stroke="#fff" stroke-width="2"/></svg>Compatibility</li>
  </ul>
  <a class="abs btn" href="#">Read More</a>
  <div class="abs visual" role="img" aria-label="Smartphone showing the KORA app device list"></div>
  <div class="dots" style="top:160px"><span></span><span></span><span></span><span></span><span class="on"></span></div>
</section>

<section class="specs band-light sep">
  <div class="abs visual" role="img" aria-label="KORA bulb glowing yellow"></div>
  <h2 class="abs title">KORA technical specifications</h2>
  <ul class="dot-list">
    <li>KORA lightbulb is a 9W LED equivalent that transforms your visual environment.</li>
    <li>E27 socket: no need to change anything, easy to fit in any home lamp.</li>
    <li>16 million colors and 600 lumens from an energy efficient LED.</li>
    <li>2700-5500K: warm or cold light depending on your activities.</li>
  </ul>
</section>

<footer class="site-footer">
  <h2>CONNECT WITH US</h2>
  <div class="social" aria-label="Social links"><span></span><span></span><span></span><span></span><span></span></div>
  <div class="rule"></div>
  <small>Trademark Ltd. 2014 ©</small>
</footer>

</body>
</html>
```